Post Disaster Temporary Housing Literature Review poster

Wanting a poster design for two Emergency Management conferences we have coming up. The information to be included in the poster is capturing the purpose, findings and recommendations from a post disaster temporary housing literature review looking at “What should government consider in order to improve planning and decision making for accommodation needs after a disaster, and to support people’s transition to stable housing?”
I’d like to enhance the visual appeal through including relevant images or graphic. I am also open to reducing the text if needed.
The government group I work with focuses on the social and human side of disaster recovery so keen for any images to reflect the human aspect and not focus solely on disasters or housing.
Government and NGO's

```html
<!DOCTYPE html>
<html lang="en">
<head>
<meta charset="utf-8">
<title>Post Disaster Temporary Housing Literature Review</title>
<link rel="stylesheet" href="https://fonts.googleapis.com/css2?family=Poppins:wght@400;500;600;700;800&display=swap">
<style>
:root{
  --purple:#9c1b8b;
  --ink:#1f1f22;
  --slate:#8c9cb2;
  --panel-light:#95a9bc;
  --panel-dark:#7b91a8;
  --backdrop:#b3b7bb;
  --white:#ffffff;
  --url:#aab6c6;
}
*{box-sizing:border-box;margin:0;padding:0}
html,body{width:769px;height:1200px;overflow:hidden;background:var(--backdrop);font-family:'Poppins',sans-serif;color:var(--ink)}
.poster{position:absolute;left:54px;top:0;width:660px;height:1200px;background:var(--white);overflow:hidden}
.abs{position:absolute}
.title-band{left:0;top:0;width:394px;height:150px;background:var(--purple);color:var(--white)}
.title{position:absolute;left:34px;top:30px;font-size:27px;line-height:32px;font-weight:800;text-transform:uppercase;letter-spacing:-0.2px}
.title .light{font-weight:500}
.hero{left:394px;top:0;width:266px;height:150px;background:linear-gradient(170deg,#5f7f99 0%,#88a6bb 45%,#b35a48 72%,#9cc25a 100%)}
.info-band{left:0;top:150px;width:660px;height:58px;background:var(--ink);color:var(--white)}
.report-label{position:absolute;left:34px;top:13px;font-size:17px;line-height:18px;font-weight:500}
.report-date{position:absolute;left:34px;top:33px;font-size:15px;line-height:16px;letter-spacing:5.6px;color:var(--slate);font-weight:500}
.band-divider{position:absolute;left:218px;top:15px;width:1px;height:33px;background:var(--purple)}
.full-label{position:absolute;left:233px;top:15px;font-size:9px;letter-spacing:2.4px;font-weight:500;white-space:nowrap}
.full-url{position:absolute;left:233px;top:31px;width:420px;font-size:10px;line-height:14px;color:var(--url);font-weight:500;white-space:nowrap}

.section-head{font-weight:700;color:var(--slate);font-size:21px;line-height:24px}
.body-text{font-size:7.8px;line-height:9.4px}
.purpose-head{left:76px;top:232px}
.purpose-icon{left:35px;top:227px}
.purpose-text{left:35px;top:265px;width:290px}
.question{left:35px;top:344px;width:290px}
.question-mark{position:absolute;left:0;top:-2px;font-size:30px;line-height:30px;font-weight:800;color:var(--purple)}
.question p{margin-left:17px;font-weight:700;font-size:7.8px;line-height:9.4px}
.commission{left:36px;top:380px;width:290px}
.rec-icon{left:35px;top:432px}
.rec-head{left:78px;top:437px;font-size:22px}

.timeline{left:57px;top:500px;height:620px;border-left:1px dashed #666}
.rec{position:absolute;left:36px;width:300px}
.rec svg{position:absolute;left:0;top:4px}
.rec h3{margin-left:51px;font-size:11px;line-height:14px;font-weight:700;color:var(--purple)}
.rec p{margin-left:52px;font-size:7.8px;line-height:9.4px;margin-top:1px}
.research-list{position:absolute;left:87px;top:909px;width:250px;display:grid;grid-template-columns:114px 114px;column-gap:0;row-gap:6px;list-style:none}
.research-list li{position:relative;padding-left:9px;font-size:5.9px;line-height:7px}
.research-list li::before{content:"";position:absolute;left:0;top:1.5px;width:4px;height:4px;border-radius:50%;background:var(--purple)}

.findings{left:343px;top:213px;width:317px;height:696px;border-radius:14px 0 0 14px;overflow:hidden;background:var(--panel-light);color:var(--white)}
.band-dark{position:absolute;left:0;top:217px;width:317px;height:254px;background:var(--panel-dark)}
.findings-icon{left:26px;top:16px}
.findings-head{left:72px;top:18px;font-size:22px;line-height:26px;font-weight:700;color:var(--purple)}
.tile{position:absolute;left:26px;width:43px;height:43px;border-radius:6px;background:var(--ink)}
.tile svg{position:absolute;left:8px;top:8px}
.sub-head{position:absolute;left:83px;font-size:14.6px;line-height:17px;font-weight:700}
.panel-text{position:absolute;left:24px;width:262px;font-size:7.8px;line-height:9.4px}
.tick-list{position:absolute;left:24px;width:260px;list-style:none}
.tick-list li{position:relative;padding-left:13px;font-size:7.8px;line-height:9.4px}
.tick-list li::before{content:"";position:absolute;left:0;top:1.5px;width:7px;height:7px;border-radius:50%;background:var(--ink)}
.tick-list li::after{content:"";position:absolute;left:2px;top:3px;width:2.5px;height:1.5px;border-left:1px solid #fff;border-bottom:1px solid #fff;transform:rotate(-45deg)}

.next-icon{left:360px;top:919px}
.next-head{left:405px;top:926px}
.next-text{left:360px;top:963px;width:262px}
.org-mark{left:366px;top:1040px;width:38px;height:38px;border-radius:50%;border:3px solid #3f9fb1}
.org-name{left:350px;top:1082px;width:78px;text-align:center;font-size:7.6px;line-height:9px;color:var(--ink)}
.contact-head{left:434px;top:1030px;font-size:15px;line-height:18px;font-weight:700;color:var(--purple)}
.contact-lines{left:434px;top:1074px;font-size:8.2px;line-height:14px;font-weight:600;font-style:normal}
.email-bar{left:360px;top:1133px;width:300px;height:21px;background:var(--ink);color:var(--white);font-size:10.4px;line-height:21px;font-weight:700;padding-left:10px;white-space:nowrap}
.mail-dot{left:353px;top:1138px;width:11px;height:11px;border-radius:50%;background:var(--purple)}
</style>
</head>
<body>
<main class="poster">
  <header>
    <div class="abs title-band">
      <h1 class="title"><span class="light">Post Disaster</span><br>Temporary Housing<br>Literature Review</h1>
    </div>
    <div class="abs hero" role="img" aria-label="Illustration of a tornado tearing apart a red house under a stormy sky"></div>
    <div class="abs info-band">
      <div class="report-label">SUMMARY REPORT</div>
      <div class="report-date">JANUARY 2024</div>
      <div class="band-divider"></div>
      <div class="full-label">THE FULL REPORT IS AVAILABLE AT</div>
      <div class="full-url">https://library.recoveryhub.example/resources/community-recovery-group</div>
    </div>
  </header>

  <section class="purpose">
    <svg class="abs purpose-icon" width="36" height="34" viewBox="0 0 36 34" aria-hidden="true">
      <circle cx="16" cy="18" r="14" fill="none" stroke="#9c1b8b" stroke-width="3"/>
      <circle cx="16" cy="18" r="8.5" fill="none" stroke="#9c1b8b" stroke-width="3"/>
      <circle cx="16" cy="18" r="3" fill="#9c1b8b"/>
      <path d="M16 18 L31 4 M27 2 L33 2 L33 8" fill="none" stroke="#9c1b8b" stroke-width="2.6" stroke-linecap="round"/>
    </svg>
    <h2 class="abs section-head purpose-head">Purpose</h2>
    <p class="abs body-text purpose-text">There are currently significant challenges in supporting displaced people with timely and equitable access to emergency and temporary accommodation and assisting them on a path to stable housing in the aftermath of a disaster. This report seeks to support agencies and decision makers to formulate and implement appropriate approaches to post-disaster housing, factoring in the scale of a disaster and varying community cohorts. The central research question underpinning this report is:</p>
    <div class="abs question">
      <span class="question-mark">?</span>
      <p>What should government consider in order to improve planning and decision making for accommodation needs after a disaster, and to support people’s transition to stable housing?</p>
    </div>
    <p class="abs body-text commission">The full report was commissioned by the Community Recovery Advisory Group (CRAG) and undertaken by Helena Marsden and Peter Callow through the Southern Coast Institute of Technology (SCIT). The findings and recommendations may be utilised by stakeholders.</p>
  </section>

  <section class="recommendations">
    <svg class="abs rec-icon" width="40" height="38" viewBox="0 0 40 38" aria-hidden="true">
      <rect x="2" y="19" width="7" height="16" fill="none" stroke="#9c1b8b" stroke-width="2.4"/>
      <path d="M9 21 L15 13 L17 5 Q21 4 21 10 L20 16 L30 16 Q33 17 31 21 Q33 23 30 25 Q32 28 28 29 Q30 32 26 34 L9 34" fill="none" stroke="#9c1b8b" stroke-width="2.4" stroke-linejoin="round"/>
      <path d="M26 3 L28 7 M34 7 L31 10 M36 14 L32 14 M20 1 L20 3" stroke="#9c1b8b" stroke-width="2" stroke-linecap="round"/>
    </svg>
    <h2 class="abs section-head rec-head">Recommendations</h2>
    <div class="abs timeline"></div>

    <div class="rec" style="top:477px">
      <svg width="44" height="40" viewBox="0 0 44 40" aria-hidden="true"><polygon points="11,1 33,1 43,20 33,39 11,39 1,20" fill="#1f1f22" stroke="#9c1b8b" stroke-width="1.6"/><circle cx="22" cy="18" r="7" fill="none" stroke="#fff" stroke-width="1.2"/><path d="M12 28 L22 25 L32 28" fill="none" stroke="#fff" stroke-width="1.2"/></svg>
      <h3>Terminology</h3>
      <p>Develop a standard set of terminology to describe the phases and types of accommodation displaced people may access on the path to stable housing and to be adopted by State and Territory recovery agencies. The terms recommended for consideration are: Emergency and Short-Term Accommodation, Temporary Housing and Stable Housing.</p>
    </div>
    <div class="rec" style="top:568px">
      <svg width="44" height="40" viewBox="0 0 44 40" aria-hidden="true"><polygon points="11,1 33,1 43,20 33,39 11,39 1,20" fill="#1f1f22" stroke="#9c1b8b" stroke-width="1.6"/><rect x="14" y="11" width="12" height="16" fill="none" stroke="#fff" stroke-width="1.2"/><path d="M27 21 L32 23 L32 27 Q29 31 27 31 Q25 31 22 27" fill="none" stroke="#fff" stroke-width="1.2"/></svg>
      <h3>Principles</h3>
      <p>Adopt common principles of leading practice in post-disaster housing recovery including community connection, wellbeing, liveability, viability, and sustainability, for deciding accommodation and support options for people.</p>
    </div>
    <div class="rec" style="top:643px">
      <svg width="44" height="40" viewBox="0 0 44 40" aria-hidden="true"><polygon points="11,1 33,1 43,20 33,39 11,39 1,20" fill="#1f1f22" stroke="#9c1b8b" stroke-width="1.6"/><rect x="14" y="10" width="13" height="18" fill="none" stroke="#fff" stroke-width="1.2"/><path d="M17 15 H24 M17 19 H24 M17 23 H21" stroke="#fff" stroke-width="1.1"/><circle cx="29" cy="26" r="4" fill="none" stroke="#fff" stroke-width="1.2"/></svg>
      <h3>National Principles</h3>
      <p>The Commonwealth and State/Territory governments should extend the agreed principles of disaster recovery to include principles of resilient recovery.</p>
    </div>
    <div class="rec" style="top:699px">
      <svg width="44" height="40" viewBox="0 0 44 40" aria-hidden="true"><polygon points="11,1 33,1 43,20 33,39 11,39 1,20" fill="#1f1f22" stroke="#9c1b8b" stroke-width="1.6"/><rect x="15" y="10" width="14" height="20" rx="1" fill="none" stroke="#fff" stroke-width="1.2"/><path d="M18 15 H26 M18 19 H26 M18 23 H26 M18 27 H23" stroke="#fff" stroke-width="1.1"/></svg>
      <h3>Guidelines</h3>
      <p>Develop resources and guidelines to support planning and operational response for post disaster temporary housing.</p>
    </div>
    <div class="rec" style="top:754px">
      <svg width="44" height="40" viewBox="0 0 44 40" aria-hidden="true"><polygon points="11,1 33,1 43,20 33,39 11,39 1,20" fill="#1f1f22" stroke="#9c1b8b" stroke-width="1.6"/><circle cx="22" cy="20" r="9" fill="none" stroke="#fff" stroke-width="1.2"/><path d="M18 16 L26 24 M26 16 L18 24" stroke="#fff" stroke-width="1.1"/></svg>
      <h3>Capacity Building</h3>
      <p>Develop capacity building resources and programs for State/Territory agencies and local governments to support pre planning for disaster temporary housing.</p>
    </div>
    <div class="rec" style="top:811px">
      <svg width="44" height="40" viewBox="0 0 44 40" aria-hidden="true"><polygon points="11,1 33,1 43,20 33,39 11,39 1,20" fill="#1f1f22" stroke="#9c1b8b" stroke-width="1.6"/><circle cx="22" cy="18" r="8" fill="none" stroke="#fff" stroke-width="1.2"/><path d="M22 13 V23 M19.5 15.5 Q22 14 24.5 15.5 M19.5 20.5 Q22 22 24.5 20.5" fill="none" stroke="#fff" stroke-width="1.1"/><path d="M13 30 Q22 25 31 30" fill="none" stroke="#fff" stroke-width="1.2"/></svg>
      <h3>Funding</h3>
      <p>Recognise different cost implications of temporary housing programs including indirect costs. Develop funding streams to address the priority needs.</p>
    </div>
    <div class="rec" style="top:866px">
      <svg width="44" height="40" viewBox="0 0 44 40" aria-hidden="true"><polygon points="11,1 33,1 43,20 33,39 11,39 1,20" fill="#1f1f22" stroke="#9c1b8b" stroke-width="1.6"/><rect x="12" y="11" width="18" height="14" fill="none" stroke="#fff" stroke-width="1.2"/><circle cx="25" cy="22" r="4.5" fill="none" stroke="#fff" stroke-width="1.2"/><path d="M28 25 L32 29" stroke="#fff" stroke-width="1.4"/></svg>
      <h3>Further Research</h3>
      <p>Undertake research into post disaster temporary housing topics such as:</p>
    </div>
    <ul class="research-list">
      <li>Improving housing resilience through land-use planning and building codes.</li>
      <li>Utilisation of innovative construction technologies, materials and methods.</li>
      <li>Learnings from previous disasters on suitable approaches for different communities and contexts.</li>
      <li>Utilising permanent prefabricated housing modules that transition from temporary to permanent.</li>
    </ul>
    <div class="rec" style="top:976px">
      <svg width="44" height="40" viewBox="0 0 44 40" aria-hidden="true"><polygon points="11,1 33,1 43,20 33,39 11,39 1,20" fill="#1f1f22" stroke="#9c1b8b" stroke-width="1.6"/><circle cx="26" cy="18" r="6" fill="none" stroke="#fff" stroke-width="1.2" stroke-dasharray="2 1.5"/><circle cx="26" cy="18" r="2" fill="#fff"/><path d="M13 28 Q16 20 21 24" fill="none" stroke="#fff" stroke-width="1.2"/></svg>
      <h3>Pilot Project</h3>
      <p>Resource, trial and evaluate a pilot program to identify ways of achieving a two-phase approach to assisting home-owners and renter households into stable housing.</p>
    </div>
    <div class="rec" style="top:1036px">
      <svg width="44" height="40" viewBox="0 0 44 40" aria-hidden="true"><polygon points="11,1 33,1 43,20 33,39 11,39 1,20" fill="#1f1f22" stroke="#9c1b8b" stroke-width="1.6"/><circle cx="18" cy="15" r="4" fill="none" stroke="#fff" stroke-width="1.2"/><circle cx="27" cy="15" r="4" fill="none" stroke="#fff" stroke-width="1.2"/><path d="M13 30 L16 22 L20 26 M31 30 L28 22 L24 26" fill="none" stroke="#fff" stroke-width="1.2"/></svg>
      <h3>Decision Making Framework</h3>
      <p>Adopt the outline of a Decision-Making Framework for Disaster Housing Recovery provided in this report to provide a basis for the development of tools that can be used by multiple stakeholders in housing recovery programs and projects across different parts of Australia.</p>
    </div>
    <div class="rec" style="top:1116px">
      <svg width="44" height="40" viewBox="0 0 44 40" aria-hidden="true"><polygon points="11,1 33,1 43,20 33,39 11,39 1,20" fill="#1f1f22" stroke="#9c1b8b" stroke-width="1.6"/><circle cx="22" cy="13" r="3.5" fill="none" stroke="#fff" stroke-width="1.2"/><path d="M12 20 L22 23 L32 20 V30 L22 32 L12 30 Z M22 23 V32" fill="none" stroke="#fff" stroke-width="1.2"/></svg>
      <h3>Capturing Learnings</h3>
      <p>Establish a national repository of evaluation reports and support processes for regular cross-case analysis.</p>
    </div>
  </section>

  <section class="abs findings">
    <div class="band-dark"></div>
    <svg class="abs findings-icon" width="30" height="32" viewBox="0 0 30 32" aria-hidden="true">
      <rect x="1.5" y="1.5" width="27" height="29" rx="4" fill="none" stroke="#fff" stroke-width="2.2"/>
      <path d="M1.5 9 H28.5" stroke="#fff" stroke-width="2"/>
      <circle cx="19" cy="5.3" r="1" fill="#fff"/><circle cx="22.5" cy="5.3" r="1" fill="#fff"/><circle cx="26" cy="5.3" r="1" fill="#fff"/>
      <circle cx="15" cy="19" r="4.5" fill="none" stroke="#1f1f22" stroke-width="2"/>
      <path d="M11.5 22.5 L7.5 26.5" stroke="#1f1f22" stroke-width="2.2" stroke-linecap="round"/>
    </svg>
    <h2 class="abs findings-head">Findings</h2>

    <div class="tile" style="top:56px"><svg width="27" height="27" viewBox="0 0 27 27" aria-hidden="true"><path d="M3 25 V6 H11 V25 M11 25 V2 H20 V25 M2 25 H25" fill="none" stroke="#fff" stroke-width="1.2"/><path d="M5 9 H9 M5 13 H9 M14 6 H18 M14 10 H18 M14 14 H18" stroke="#fff" stroke-width="1"/></svg></div>
    <h3 class="sub-head" style="top:60px">Leading practice in<br>disaster housing recovery</h3>
    <p class="panel-text" style="top:111px">The analysis of leading practices in housing recovery led to the development of a checklist of actions that could be used to identify appropriate actions by housing recovery officers and their agencies in providing and managing emergency and short-term accommodation and temporary housing. The checklist was developed from research and contains criteria for achieving eight categories of leading practice: Community Engagement &amp; Participation, Location, Safety, Health, Comfort &amp; Privacy, Cultural &amp; Special Needs, Community &amp; Connection, and Social &amp; Technical Support Services.</p>

    <div class="tile" style="top:226px"><svg width="27" height="27" viewBox="0 0 27 27" aria-hidden="true"><path d="M3 12 L10 5 L17 12 M5 10 V22 H15 V10 M13 17 L20 12 L26 17 M15 22 H25 V16" fill="none" stroke="#fff" stroke-width="1.2"/><rect x="8" y="15" width="4" height="7" fill="none" stroke="#fff" stroke-width="1"/></svg></div>
    <h3 class="sub-head" style="top:230px">Innovative approaches<br>to temporary housing</h3>
    <p class="panel-text" style="top:282px">Innovative approaches to effective temporary housing practices are based upon the concept of resilient housing recovery, which has at least five dimensions: Wellbeing, Liveability, Sustainability, Community Connection, and Viability. This change of focus has two major implications:</p>
    <ul class="tick-list" style="top:332px">
      <li>The planning of post-disaster housing and infrastructure programs needs to be become one of the priority strategies in pre-disaster preparation; and</li>
      <li style="margin-top:9px">Strategies are needed to establish Temporary Housing as the first step in the design and construction of on-site Stable Housing to minimise the social, economic and environmental costs incurred when displaced people spend extended periods of time in Temporary Housing.</li>
    </ul>
    <p class="panel-text" style="top:421px">These implications are explored through strategies and tools for pre-disaster planning and the development of a two-phase model for constructing Stable Housing through a “temporary-to-permanent” construction strategy.</p>

    <div class="tile" style="top:492px"><svg width="27" height="27" viewBox="0 0 27 27" aria-hidden="true"><path d="M6 12 L13.5 5 L21 12 V19 H6 Z" fill="none" stroke="#fff" stroke-width="1.2"/><rect x="11" y="13" width="5" height="6" fill="none" stroke="#fff" stroke-width="1"/><path d="M2 18 Q4 24 10 24 H20 Q24 23 25 19" fill="none" stroke="#fff" stroke-width="1.2"/></svg></div>
    <h3 class="sub-head" style="top:490px">A decision-making<br>framework for resilient<br>housing recovery</h3>
    <p class="panel-text" style="top:551px">The Framework seeks to integrate the steps in project management and to use the housing process as a lever for overall recovery. This involves aligning decisions at strategic and operational levels and managing the trade-offs between issues of location, tenure, housing types and procurement.</p>
    <p class="panel-text" style="top:607px">There are nine such decision categories in the Framework: Consultation, Pre-Disaster Planning for Housing Recovery, Situation Analysis after a Disaster Event, Recognising Cohorts of Displaced People with Different Needs and Assets, Identifying and Selecting Housing Model Options; Providing AgencyWrap-Around Support Services; Using Housing Decisions to Promote Local Economic and Social Recovery, Program Design and Delivery, and Monitoring and Evaluation.</p>
  </section>

  <section class="next-steps">
    <svg class="abs next-icon" width="38" height="36" viewBox="0 0 38 36" aria-hidden="true">
      <path d="M2 34 H36 M2 34 V27 H14 V20 H26" fill="none" stroke="#9c1b8b" stroke-width="2"/>
      <path d="M12 2 L14 12 L22 14 Q28 15 28 19 H12 Z" fill="none" stroke="#9c1b8b" stroke-width="2" stroke-linejoin="round"/>
    </svg>
    <h2 class="abs section-head next-head">Next Steps</h2>
    <p class="abs body-text next-text">The Community Recovery Advisory Group is partnering with Hazard Resilience Research Network to analyse previous post-disaster temporary housing assistance and support mechanisms used in Australia. The project aims to provide national guidance on the design and implementation of temporary housing from the research and resources developed.</p>
  </section>

  <section class="contact">
    <div class="abs org-mark"></div>
    <div class="abs org-name">Community Recovery Advisory Group</div>
    <h2 class="abs contact-head">For further<br>information contact</h2>
    <address class="abs contact-lines">Miriam Ashdown<br>National Consultant Disaster Recovery<br>Community Recovery Advisory Group</address>
    <div class="abs email-bar">miriam.ashdown@recoveryoffice.example</div>
    <div class="abs mail-dot"></div>
  </section>
</main>
</body>
</html>
```